Dental practice Re-design and relaunch the website while retaining the CI

We need a re-desgin of our totally obsolete and poorly maintained page (it was problematic to make changes). The wish is that we get a contemporary design and above all the site can update itself without much know-how about web techniques have to have. The current website: www.praxis-morlindau.de Pictures are then made available and made available.

Target Market(s)

patient information

Number of Pages Required

1 page

Font styles to use
Sans Serif

Colors

Designer to choose colors to be used in the design.

Requirements
Must have
• An area that we can revitalize ourselves with little effort!
Should not have
• Animations or similar

```html
<!DOCTYPE html>
<html lang="de">
<head>
<meta charset="utf-8">
<title>Zahnärztliche Praxis Morlindau</title>
<link rel="stylesheet" href="https://fonts.googleapis.com/css2?family=Raleway:wght@300;400;500&family=Open+Sans:wght@400;600&display=swap">
<style>
:root{
  --green-light:#8bd46a;
  --green-dark:#4e9431;
  --green-text:#5aa63a;
  --ink:#222;
  --body:#333;
  --grey-bg:#f7f7f7;
  --footer:#acacac;
  --white:#fff;
}
*{margin:0;padding:0;box-sizing:border-box}
html,body{width:1200px;height:2628px;overflow:hidden}
body{position:relative;background:var(--white);font-family:"Open Sans",Arial,sans-serif;color:var(--body)}
.abs{position:absolute}
/* header */
.site-header{left:0;top:0;width:1200px;height:115px;background:var(--white)}
.brand{left:160px;top:58px;text-align:center;font-family:"Raleway",sans-serif;font-weight:400;color:#333;width:200px}
.brand .line1{font-size:13px;letter-spacing:.5px}
.brand .line2{font-size:27px;letter-spacing:1px;line-height:1.1}
.brand-dot{left:246px;top:14px;width:28px;height:28px;border-radius:50%;background:#222}
.topbar{right:162px;top:24px;font-size:13px;display:flex;align-items:center;gap:16px}
.topbar .phone{color:var(--green-text);display:flex;align-items:center;gap:6px}
.topbar .sep{width:1px;height:22px;background:#ddd}
.topbar .lang{font-size:11px;color:#333;display:flex;align-items:center;gap:6px}
.main-nav{right:162px;top:79px;display:flex;gap:0;font-size:11.5px;color:#222;letter-spacing:.3px}
.main-nav a{color:inherit;text-decoration:none;margin-left:50px}
/* hero */
.hero{left:0;top:115px;width:1200px;height:540px;overflow:hidden}
.hero-photo{width:100%;height:100%;background:radial-gradient(ellipse at 28% 40%,#a57865 0%,#d9c7bc 25%,#ece8e5 55%,#d6d3d2 100%)}
.hero-curve{left:0;top:560px;width:1200px;height:100px}
.hero-title{right:162px;top:305px;text-align:right;font-family:"Raleway",sans-serif;font-weight:300;font-size:54px;line-height:1.05;color:#1a1a1a}
.btn{right:162px;top:438px;width:216px;height:46px;background:var(--green-dark);color:var(--white);font-size:13px;display:flex;align-items:center;justify-content:center;letter-spacing:.3px}
.slider-arrow{top:300px;width:48px;height:72px;background:rgba(150,150,150,.55);display:flex;align-items:center;justify-content:center}
/* features */
.features{left:0;top:620px;width:1200px;height:345px;background:var(--grey-bg)}
.cards{left:162px;top:636px;width:876px;height:276px;display:flex}
.card{width:219px;height:100%;color:var(--white);text-align:center;padding-top:56px}
.card:nth-child(odd){background:var(--green-light)}
.card:nth-child(even){background:var(--green-dark)}
.card svg{display:block;margin:0 auto}
.card h3{font-family:"Raleway",sans-serif;font-weight:400;font-size:15px;margin-top:22px;letter-spacing:.3px}
.card p{font-size:10.5px;line-height:1.6;margin:14px 32px 0}
/* content rows */
.photo{background:linear-gradient(135deg,#cfe0ea,#9fb6c4)}
.row-title{font-family:"Raleway",sans-serif;font-weight:400;font-size:21px;line-height:1.35;color:var(--ink)}
.row-text{font-size:11px;line-height:1.95;color:var(--body)}
.row-text p+p{margin-top:20px}
/* green band */
.band{left:0;top:1384px;width:1200px;height:399px;overflow:hidden}
.band-photo{width:100%;height:100%;background:linear-gradient(90deg,#b8d98a 0%,#9fcf6a 30%,#c9d8b8 60%,#8aa6c4 80%,#6d8a6a 100%)}
.notch{left:570px;width:60px;height:26px}
.band-title{left:162px;top:1494px;font-family:"Raleway",sans-serif;font-size:18px;color:var(--ink)}
.band-text{left:162px;top:1536px;width:480px;font-size:10.5px;line-height:2;color:#222}
/* closing strip */
.closing{left:0;top:2205px;width:1200px;height:141px;background:var(--green-light);color:var(--white);text-align:center;font-family:"Raleway",sans-serif;font-size:16px;line-height:1.95;padding-top:42px}
/* footer */
.site-footer{left:0;top:2346px;width:1200px;height:282px;background:var(--footer);color:var(--white)}
.footer-brand{left:160px;top:2470px;width:200px;text-align:center;font-family:"Raleway",sans-serif;font-weight:400;color:var(--white)}
.footer-brand .line1{font-size:12px;letter-spacing:.5px}
.footer-brand .line2{font-size:24px;letter-spacing:1px;line-height:1.1}
.footer-dot{left:248px;top:2420px;width:26px;height:26px;border-radius:50%;background:var(--white)}
.fcol{top:2388px;font-size:11px;line-height:2}
.fcol h4{font-family:"Raleway",sans-serif;font-weight:400;font-size:12px;margin-bottom:12px;letter-spacing:.3px}
.social{display:flex;gap:6px;margin-top:10px}
.social span{width:30px;height:30px;border:1.5px solid var(--white);border-radius:50%}
.footer-rule{left:162px;top:2568px;width:876px;height:1px;background:rgba(255,255,255,.35)}
.copyright{left:0;top:2588px;width:1200px;text-align:center;font-size:10.5px}
</style>
</head>
<body>

<header class="site-header abs">
  <span class="brand-dot abs"></span>
  <div class="brand abs"><div class="line1">ZAHNÄRZTLICHE PRAXIS</div><div class="line2">MORLINDAU</div></div>
  <div class="topbar abs">
    <span class="phone">
      <svg width="12" height="12" viewBox="0 0 24 24"><path fill="#5aa63a" d="M6.6 10.8a15 15 0 0 0 6.6 6.6l2.2-2.2c.3-.3.7-.4 1-.2 1.1.4 2.3.6 3.6.6.6 0 1 .4 1 1V20c0 .6-.4 1-1 1A17 17 0 0 1 3 4c0-.6.4-1 1-1h3.5c.6 0 1 .4 1 1 0 1.3.2 2.5.6 3.6.1.3 0 .7-.2 1z"/></svg>
      CALL US: +49 (0) 711 / 40 52 190
    </span>
    <span class="sep"></span>
    <span class="lang">ENGLISH <svg width="9" height="6" viewBox="0 0 9 6"><path d="M0 0h9L4.5 6z" fill="#5aa63a"/></svg></span>
  </div>
  <nav class="main-nav abs">
    <a href="#">PHILOSOPHIE</a><a href="#">PRAXIS</a><a href="#">SERVICES</a><a href="#">KONTAKT</a><a href="#">ANFAHRT</a><a href="#">LINKS</a>
  </nav>
</header>

<section class="hero abs">
  <div class="hero-photo" role="img" aria-label="Lächelnde junge Frau auf hellem Sofa"></div>
</section>
<div class="slider-arrow abs" style="left:0;top:300px">
  <svg width="16" height="34" viewBox="0 0 16 34"><path d="M14 2 2 17l12 15" fill="none" stroke="#fff" stroke-width="2"/></svg>
</div>
<div class="slider-arrow abs" style="right:0;top:300px">
  <svg width="16" height="34" viewBox="0 0 16 34"><path d="M2 2l12 15L2 32" fill="none" stroke="#fff" stroke-width="2"/></svg>
</div>
<h1 class="hero-title abs">PRAXIS<br>MORLINDAU</h1>
<a class="btn abs">MAKE AN APPOINTMENT</a>

<section class="features abs"></section>
<svg class="hero-curve abs" style="top:590px" width="1200" height="60" viewBox="0 0 1200 60" preserveAspectRatio="none"><path d="M0 15 Q600 -28 1200 15 V60 H0z" fill="#f7f7f7"/></svg>

<div class="cards abs">
  <div class="card">
    <svg width="66" height="66" viewBox="0 0 64 64" fill="none" stroke="#fff" stroke-width="3"><path d="M14 8c-6 3-8 12-5 22 2 7 3 20 7 26 3 4 5-10 8-14 2-3 6-3 8 0 3 4 5 18 8 14 4-6 5-19 7-26 3-10 1-19-5-22-6-3-10 1-14 1s-8-4-14-1z"/><circle cx="40" cy="28" r="8"/><path d="M46 34l8 8"/></svg>
    <h3>FINIBUONORUM</h3>
    <p>Sed ut perspiciatis unde omnis natus error sit voluptatem accusan tium doloremque laudantim.</p>
  </div>
  <div class="card">
    <svg width="66" height="66" viewBox="0 0 64 64" fill="none" stroke="#fff" stroke-width="3"><path d="M14 8c-6 3-8 12-5 22 2 7 3 20 7 26 3 4 5-10 8-14 2-3 6-3 8 0 3 4 5 18 8 14 4-6 5-19 7-26 3-10 1-19-5-22-6-3-10 1-14 1s-8-4-14-1z"/><path d="M10 24h44M22 20v8M32 20v8M42 20v8"/></svg>
    <h3>FINIBUONORUM</h3>
    <p>Sed ut perspiciatis unde omnis natus error sit voluptatem accusan tium doloremque laudantim.</p>
  </div>
  <div class="card">
    <svg width="66" height="66" viewBox="0 0 64 64"><path fill="#fff" d="M14 8c-6 3-8 12-5 22 2 7 3 20 7 26 3 4 5-10 8-14 2-3 6-3 8 0 3 4 5 18 8 14 4-6 5-19 7-26 3-10 1-19-5-22-6-3-10 1-14 1s-8-4-14-1z"/></svg>
    <h3>FINIBUONORUM</h3>
    <p>Sed ut perspiciatis unde omnis natus error sit voluptatem accusan tium doloremque laudantim.</p>
  </div>
  <div class="card">
    <svg width="66" height="66" viewBox="0 0 64 64"><path fill="#fff" d="M24 10h16v6h-4v-2h-8v2h-4zM6 18h52v36H6z"/><path fill="#4e9431" d="M28 26h8v8h8v8h-8v8h-8v-8h-8v-8h8z"/></svg>
    <h3>FINIBUONORUM</h3>
    <p>Sed ut perspiciatis unde omnis natus error sit voluptatem accusan tium doloremque laudantim.</p>
  </div>
</div>

<div class="photo abs" style="left:162px;top:1022px;width:414px;height:302px" role="img" aria-label="Zahnärztin im weißen Kittel in der Praxis"></div>
<h2 class="row-title abs" style="left:625px;top:1033px;width:420px">Um Ihnen ein unbeschwertes Lachen zu ermöglichen geben wir unser Bestes.</h2>
<div class="row-text abs" style="left:632px;top:1108px;width:406px">
  <p>Für die meisten Menschen ist ein Zahnarztbesuch unangenehm! Warum? Sie haben schlichtweg Angst, denn in Ihrer Vergangenheit war eben dieser Besuch regelmäßig mit Schmerzen verbunden. Stellen Sie sich vor, Sie gehen zum Zahnarzt und er hat überhaupt nicht gebohrt! Das ist wahrhaftig keine Utopie sondern eher eine Vision, die durch bestimmte Vorsorgemaßnahmen bei jedem Menschen Realität werden kann!</p>
  <p>Haben wir Sie ein wenig neugierig gemacht? Schön...dann investieren Sie doch ein­fach ein paar Minuten Ihrer kostbaren Zeit, und wir zeigen Ihnen den Weg...damit auch Sie sagen können:</p>
</div>

<section class="band abs">
  <div class="band-photo" role="img" aria-label="Lachendes Paar vor grünem Hintergrund"></div>
</section>
<svg class="notch abs" style="top:1384px" viewBox="0 0 60 26"><path d="M0 0h60L30 26z" fill="#fff"/></svg>
<h2 class="band-title abs">"Karies, Parodontose? Nein, Danke! "</h2>
<div class="band-text abs">Unsere Praxis ist stark auf eine Zahngesundheitsvorsorge ausgerichtet. Diese präventiven Maßnahmen fangen mit der Aufklärung einer werdenden Mutter an und hören praktisch nie auf. In ausführlichen Mundhygieneunterweisungen erhalten Sie zum einen Informationen über die Kariesentstehung zum anderen gezielte Pflegetips zur Verbesserung der häuslichen Reinigung, in Verbindung mit einer regelmäßigen professionellen Zahnreinigung. Herausnehmbarer Zahnersatz bedarf ebenso wie natürliche Zähne der regelmäßigen Überprüfung und eventueller Korrekturen und Wartungsarbeiten, wie zB. eine Unterfütterung.</div>

<div class="photo abs" style="left:162px;top:1838px;width:414px;height:302px;background:linear-gradient(135deg,#3f6fa8,#9fc3e0 45%,#e9eef2 70%,#4d88c9)" role="img" aria-label="Zahnarzt mit Mundschutz bei der Behandlung"></div>
<h2 class="row-title abs" style="left:625px;top:1848px;width:380px">In der Kariestherapie gilt für uns der Vorsatz:</h2>
<div class="row-text abs" style="left:630px;top:1930px;width:410px">
  <p>Minimalinvasiv präparieren, das heißt möglichst viel gesunde Zahnsubstanz zu erhalten und die Restauration möglichst klein zu halten. Dazu kommen in unserer Praxis optische Hilfsgeräte wie eine Lupenbrille oder das Dentalmikroskop mit bis zu 24fachen Vergrößerung zum Einsatz.</p>
  <p>Mit Hilfe moderner Technik verliert auch die ungeliebte Wurzelkanalbehandlung, Endodontie genannt, ihren Schrecken. Moderne Aufbereitungstechniken und eine strukturierte Arbeitsweise bringen vorhersagbare Ergebnisse. Wir benutzen nur geprüfte und biologisch verträgliche Materialien. Röntgenbilder werden mit der strahlungsarmen Digitaltechnik erstellt.</p>
</div>

<section class="closing abs">Insgesamt steht bei uns der Mensch im Vordergrund.<br>Um Ihnen wieder ein unbeschwertes Lachen zu ermöglichen geben wir unser Bestes.</section>
<svg class="notch abs" style="top:2205px" viewBox="0 0 60 26"><path d="M0 0h60L30 26z" fill="#fff"/></svg>

<footer class="site-footer abs"></footer>
<span class="footer-dot abs"></span>
<div class="footer-brand abs"><div class="line1">ZAHNÄRZTLICHE PRAXIS</div><div class="line2">MORLINDAU</div></div>
<div class="fcol abs" style="left:368px;color:#fff">
  <h4>HELP US</h4>
  Glac scelerisquirin<br>Dit ametconsectet<br>Sed ut perspitis nde<br>Wius error situptat<br>Saccusantiu<br>Gdoloremque
</div>
<div class="fcol abs" style="left:563px;color:#fff">
  <h4>SERVICES</h4>
  Lorem ipsum dolor<br>Dit ametconsectetur<br>adipiscing elitestibuscipit<br>ligula ac scelerisquirin<br>Dit ametconsectetur<br>adipiscing elitestibu.
</div>
<div class="fcol abs" style="left:747px;color:#fff">
  <h4>COMPANY</h4>
  Home<br>About us<br>Services<br>Portfolio<br>Contact us
</div>
<div class="fcol abs" style="left:885px;color:#fff">
  <h4>HELP &amp; CONTACT</h4>
  Email: info@praxis-morlindau.de<br>Phone: +49 (0) 711 / 40 52 190
  <div class="social"><span></span><span></span><span></span><span></span></div>
</div>
<div class="footer-rule abs"></div>
<div class="copyright abs" style="color:#fff">© 2017. All Copyrights are Reserved.Privacy | Terms &amp; Conditions</div>

</body>
</html>
```